Lien Post Card - (5.5 x 8.5)

FRONT OF POSTCARD
Is a Property Lien Putting Your Home at Risk?
HOA Liens • Tax Liens • Municipal Charges • Other Property-Related Liens
You may have options to resolve outstanding liens and protect your home.
A Refinance or Home Equity Line of Credit (HELOC) may help you:
✔ Pay off qualifying liens
✔ Consolidate debt into one manageable payment
✔ Access your home's equity
✔ Improve your financial flexibility
✔ Avoid additional penalties, fees, or collection actions
Don't wait until the situation becomes more difficult.
Call today for a confidential review of your options.
Bluecove Lending Group, Inc.
(800) 641-2907 x 42
www.bluecovelending.com
NMLS #738150
BACK OF POSTCARD
Your Home Equity Could Be the Solution
If you have received notices regarding:
• Delinquent Property Taxes
• HOA or Condo Association Assessments
• Municipal Utility Liens
• Special Assessments
• Other Property-Related Obligations
You may qualify for financing options designed to help satisfy those obligations and bring your property current.
Our experienced mortgage professionals can review your situation and discuss available programs, including:
• Cash-Out Refinancing
• Home Equity Lines of Credit (HELOCs)
• Home Equity Loans
• Debt Consolidation Solutions
Free Consultation • No Obligation
Contact Marcus Whitfield today at (800) 641-2907 x42 or mwhitfield@bluecovelending.com (NMLS #84617)

```html
<!DOCTYPE html>
<html lang="en">
<head>
<meta charset="utf-8">
<title>Lien Postcard – Front and Back</title>
<link href="https://fonts.googleapis.com/css2?family=Noto+Serif:wght@400;700&family=Dancing+Script:wght@700&display=swap" rel="stylesheet">
<style>
:root{
  --stage:#2d3a57;
  --navy:#0f2a6e;
  --blue:#1e4fa8;
  --blue-bright:#2f6fd6;
  --blue-deep:#0b2a7a;
  --gold:#c9953f;
  --gold-light:#f0c987;
  --gold-pill:#e8b96a;
  --ink:#1b1b1b;
  --paper:#f6f6f6;
  --white:#ffffff;
}
*{margin:0;padding:0;box-sizing:border-box}
html,body{width:903px;height:1200px;overflow:hidden;background:var(--stage)}
body{position:relative;font-family:"Noto Serif",Georgia,serif;color:var(--ink)}
.nowrap{white-space:nowrap}
.card{position:absolute;left:61px;width:780px;height:504px;background:var(--paper);overflow:hidden}
.card--front{top:80px}
.card--back{top:617px;height:505px}
.abs{position:absolute}

/* front */
.brand{left:48px;top:46px;display:flex;align-items:center;gap:7px;font-weight:700;font-size:13px;color:var(--navy);line-height:1.15}
.brand-dot{width:20px;height:20px;border-radius:50%;background:var(--gold);flex:none}
.headline{left:194px;top:30px;font-size:26px;font-weight:700;line-height:1.14;color:var(--navy);letter-spacing:-.2px}
.headline .gold{color:var(--gold)}
.headline .blue{color:var(--blue)}
.tags{left:59px;top:110px;display:flex;gap:7px}
.tag{background:var(--blue-deep);color:var(--white);font-size:13px;padding:3px 4px;border-radius:3px;height:24px;line-height:18px;white-space:nowrap}
.intro{left:60px;top:142px;font-size:11.5px}
.benefits-title{left:59px;top:181px;font-size:14.5px;font-weight:700;color:var(--gold);line-height:1.25}
.benefit{display:flex;align-items:center;gap:9px;font-size:9.5px;font-weight:700;line-height:1.3}
.icon-badge{width:38px;height:38px;border-radius:50%;flex:none;display:flex;align-items:center;justify-content:center;box-shadow:0 2px 3px rgba(0,0,0,.25)}
.icon-badge--gold{background:radial-gradient(circle at 40% 35%,#f7d9a0,#d9a24d);border:2px solid #e9e3d8}
.icon-badge--blue{background:radial-gradient(circle at 40% 35%,#3d7ee0,#0d2d80);border:2px solid #e2b967}
.urge{left:57px;top:380px;font-size:14.5px;font-weight:700;color:var(--navy)}
.urge span{color:var(--blue-bright)}
.cta{left:56px;top:403px;width:368px;height:110px;border-radius:12px 12px 0 0;background:linear-gradient(180deg,#2f74d6,#1848a8)}
.cta-phone{left:17px;top:20px;width:34px;height:34px;border-radius:50%;background:var(--white);display:flex;align-items:center;justify-content:center}
.cta-divider{left:60px;top:16px;width:1px;height:44px;background:rgba(255,255,255,.55)}
.cta-copy{left:67px;top:12px;font-size:12.5px;font-weight:700;color:var(--white);line-height:1.27}
.cta-copy span{color:var(--gold-light)}
.cta-nmls{left:67px;top:66px;font-size:9.5px;color:var(--white);font-weight:700}
.company-pill{left:213px;top:14px;background:var(--gold-pill);border-radius:6px;font-size:8.5px;font-weight:700;color:var(--navy);padding:3px 7px;white-space:nowrap}
.contact-line{display:flex;align-items:center;gap:5px;color:var(--white);font-weight:700;white-space:nowrap}
.mini-icon{width:14px;height:14px;border-radius:50%;background:var(--gold-pill);display:flex;align-items:center;justify-content:center;flex:none}

/* back */
.equity-title{left:0;width:782px;top:15px;text-align:center;font-size:30px;font-weight:700;line-height:1.06;color:var(--gold-light)}
.stamp-box{left:686px;top:19px;width:75px;height:75px;background:var(--white);border:1px solid #d8dde6}
.notice-lead{left:49px;top:118px;font-size:12.5px;font-weight:700}
.notice-lead span{color:var(--blue-deep)}
.notice-list{left:49px;top:139px;list-style:none;font-size:10.5px;font-weight:700;line-height:12.9px}
.notice-list li::before{content:"•";color:var(--gold);margin-right:4px;font-size:9px}
.fade-rule{left:49px;top:209px;width:140px;height:6px;background:linear-gradient(90deg,#d6d6d6,rgba(214,214,214,0))}
.review-text{left:425px;top:129px;width:320px;text-align:center;font-size:10.8px;line-height:1.3;white-space:nowrap}
.programs{left:445px;top:168px;width:280px;height:116px;border-radius:15px;background:linear-gradient(180deg,#2d6fd2,#0c2f88);padding:14px 0 0 14px;list-style:none}
.programs li{display:flex;align-items:center;gap:7px;color:var(--white);font-size:11.8px;font-weight:700;height:23.7px;white-space:nowrap}
.consult-pill{left:260px;top:226px;width:123px;height:40px;border-radius:12px;background:linear-gradient(180deg,#f1c47a,#dba24e);text-align:center;font-size:11px;font-weight:700;color:var(--navy);line-height:1.3;padding-top:5px}
.contact-script{left:173px;top:245px;font-family:"Dancing Script",cursive;font-size:24px;color:var(--blue)}
.contact-name{left:177px;top:279px;font-size:16.5px;font-weight:700;color:var(--navy)}
.contact-name span{color:var(--blue-bright)}
.agent-panel{left:0;top:313px;width:390px;height:152px;border-radius:0 20px 20px 0;background:linear-gradient(180deg,#2d6cd0,#0f3a95);overflow:hidden}
.skyline{left:240px;top:60px;width:150px;height:92px;background:linear-gradient(180deg,rgba(20,50,130,0) 0%,#f0a44a 55%,#4b3a3f 100%)}
.agent-nmls{right:13px;bottom:6px;font-size:8.5px;font-weight:700;color:#8fb6ff}
.portrait{left:0;top:226px}
</style>
</head>
<body>

<!-- FRONT -->
<section class="card card--front" aria-label="Postcard front">
  <svg class="abs" style="left:0;top:0" width="780" height="504" viewBox="0 0 780 504">
    <defs>
      <linearGradient id="houseTint" x1="0" y1="0" x2="1" y2="1">
        <stop offset="0" stop-color="#2a66d8"/>
        <stop offset="1" stop-color="#7fb0f0"/>
      </linearGradient>
      <linearGradient id="coupleTone" x1="0" y1="0" x2="0" y2="1">
        <stop offset="0" stop-color="#c9b7a8"/>
        <stop offset=".45" stop-color="#5d7fb9"/>
        <stop offset="1" stop-color="#34507e"/>
      </linearGradient>
    </defs>
    <path d="M520 0 C560 80 590 180 600 270 L620 504 L780 504 L780 0 Z" fill="#e9cf9f" opacity=".6"/>
    <g role="img" aria-label="Photo of a suburban two-storey house tinted in blue">
      <path d="M555 0 C600 90 620 190 630 280 L640 504 L780 504 L780 0 Z" fill="url(#houseTint)"/>
    </g>
    <g role="img" aria-label="Photo of a worried couple sitting with bills and a calculator">
      <path d="M458 310 C470 280 500 265 540 268 C580 270 610 250 650 250 C700 250 740 270 780 300 L780 504 L470 504 Z" fill="url(#coupleTone)"/>
    </g>
  </svg>

  <div class="abs brand nowrap"><span class="brand-dot"></span>Bluecove<br>Lending Group</div>

  <h1 class="abs headline nowrap">Is a <span class="gold">Property Lien</span> Putting<br>Your Home <span class="blue">at Risk?</span></h1>

  <div class="abs tags">
    <span class="tag">HOA Liens</span>
    <span class="tag">Tax Liens</span>
    <span class="tag">Municipal Charges</span>
    <span class="tag">Other Property-Related Liens</span>
  </div>

  <p class="abs intro nowrap">You may have options to resolve outstanding liens and protect your home.</p>

  <h2 class="abs benefits-title">A Refinance or Home Equity Line of<br>Credit (HELOC) may help you:</h2>

  <div class="abs benefit" style="left:55px;top:225px">
    <span class="icon-badge icon-badge--gold"><svg width="18" height="18" viewBox="0 0 24 24"><circle cx="12" cy="12" r="9" fill="none" stroke="#fff" stroke-width="2"/><path d="M7.5 12.5l3 3 6-6" fill="none" stroke="#fff" stroke-width="2.2"/></svg></span>
    <span>Pay off qualifying liens</span>
  </div>
  <div class="abs benefit" style="left:234px;top:225px">
    <span class="icon-badge icon-badge--blue"><svg width="18" height="18" viewBox="0 0 24 24"><rect x="4" y="13" width="3" height="7" fill="#fff"/><rect x="9" y="10" width="3" height="10" fill="#fff"/><rect x="14" y="7" width="3" height="13" fill="#fff"/><path d="M19 3v9M16 6l3-3 3 3" stroke="#fff" stroke-width="2" fill="none"/></svg></span>
    <span>Improve your<br>financial flexibility</span>
  </div>
  <div class="abs benefit" style="left:55px;top:272px">
    <span class="icon-badge icon-badge--blue"><svg width="16" height="18" viewBox="0 0 20 24"><path d="M3 2h10l4 4v16H3z" fill="#fff"/><path d="M6 10h8M6 14h8M6 18h5" stroke="#1e4fa8" stroke-width="1.6"/></svg></span>
    <span>Consolidate debt into one<br>manageable payment</span>
  </div>
  <div class="abs benefit" style="left:235px;top:272px">
    <span class="icon-badge icon-badge--gold"><svg width="18" height="18" viewBox="0 0 24 24"><path d="M12 2l8 3v6c0 6-4 9-8 11-4-2-8-5-8-11V5z" fill="none" stroke="#fff" stroke-width="2"/><path d="M8.5 12l2.5 2.5 4.5-4.5" stroke="#fff" stroke-width="2" fill="none"/></svg></span>
    <span>Access your home's equity</span>
  </div>
  <div class="abs benefit" style="left:55px;top:320px">
    <span class="icon-badge icon-badge--gold"><svg width="18" height="18" viewBox="0 0 24 24"><path d="M3 12L12 4l9 8h-3v8h-4v-5h-4v5H6v-8z" fill="#fff"/></svg></span>
    <span>Avoid additional penalties,<br>fees, or collection actions</span>
  </div>

  <p class="abs urge nowrap">Don't wait until the situation becomes <span>more difficult</span>.</p>

  <div class="abs cta">
    <div class="abs cta-phone"><svg width="20" height="20" viewBox="0 0 24 24"><path d="M6.6 3.5l3 3.2-1.8 2.4c1 2.3 3 4.3 5.1 5.3l2.4-1.8 3.2 3-1.6 3.2C11 19 5 13 3.4 5.1z" fill="#1e4fa8"/></svg></div>
    <div class="abs cta-divider"></div>
    <p class="abs cta-copy nowrap"><span>Call today</span> for a<br>confidential review<br>of your options.</p>
    <p class="abs cta-nmls">NMLS #738150</p>
    <p class="abs company-pill">Bluecove Lending Group, Inc.</p>
    <div class="abs contact-line" style="left:215px;top:35px;font-size:11.5px">
      <span class="mini-icon"><svg width="9" height="9" viewBox="0 0 24 24"><path d="M6.6 3.5l3 3.2-1.8 2.4c1 2.3 3 4.3 5.1 5.3l2.4-1.8 3.2 3-1.6 3.2C11 19 5 13 3.4 5.1z" fill="#fff"/></svg></span>(800) 641-2907 x 42
    </div>
    <div class="abs contact-line" style="left:215px;top:54px;font-size:9.5px">
      <span class="mini-icon"><svg width="10" height="10" viewBox="0 0 24 24"><circle cx="12" cy="12" r="9" fill="none" stroke="#fff" stroke-width="2"/><path d="M3 12h18M12 3c3 3 3 15 0 18M12 3c-3 3-3 15 0 18" fill="none" stroke="#fff" stroke-width="1.6"/></svg></span>www.bluecovelending.com
    </div>
  </div>
</section>

<!-- BACK -->
<section class="card card--back" aria-label="Postcard back">
  <svg class="abs" style="left:0;top:0" width="780" height="130" viewBox="0 0 780 130">
    <defs>
      <linearGradient id="bandBlue" x1="0" y1="0" x2="1" y2="0">
        <stop offset="0" stop-color="#0c2f88"/>
        <stop offset="1" stop-color="#2466d0"/>
      </linearGradient>
      <linearGradient id="goldDisc" x1="0" y1="0" x2="1" y2="1">
        <stop offset="0" stop-color="#f2cf8e"/>
        <stop offset="1" stop-color="#d69a45"/>
      </linearGradient>
    </defs>
    <path d="M0 0 H780 V48 Q430 128 70 72 L0 62 Z" fill="url(#bandBlue)"/>
    <circle cx="40" cy="-2" r="78" fill="url(#goldDisc)"/>
  </svg>

  <h2 class="abs equity-title">Your Home Equity<br>Could Be the Solution</h2>
  <div class="abs stamp-box"></div>

  <p class="abs notice-lead nowrap">If you have received <span>notices regarding</span>:</p>
  <ul class="abs notice-list nowrap">
    <li>Delinquent Property Taxes</li>
    <li>HOA or Condo Association Assessments</li>
    <li>Municipal Utility Liens</li>
    <li>Special Assessments</li>
    <li>Other Property-Related Obligations</li>
  </ul>
  <div class="abs fade-rule"></div>

  <p class="abs review-text">Our experienced mortgage professionals can review your<br>situation and discuss available programs, including:</p>

  <ul class="abs programs">
    <li><span class="mini-icon"><svg width="9" height="9" viewBox="0 0 24 24"><text x="12" y="18" font-size="18" text-anchor="middle" fill="#0c2f88" font-weight="700">$</text></svg></span>Cash-Out Refinancing</li>
    <li><span class="mini-icon"><svg width="9" height="9" viewBox="0 0 24 24"><rect x="2" y="6" width="20" height="13" rx="2" fill="#0c2f88"/></svg></span>Home Equity Lines of Credit (HELOCs)</li>
    <li><span class="mini-icon"><svg width="9" height="9" viewBox="0 0 24 24"><path d="M3 12L12 4l9 8h-3v8H6v-8z" fill="#0c2f88"/></svg></span>Home Equity Loans</li>
    <li><span class="mini-icon"><svg width="9" height="9" viewBox="0 0 24 24"><path d="M2 12l5-4 5 3 5-3 5 4-5 5-5-3-5 3z" fill="#0c2f88"/></svg></span>Debt Consolidation Solutions</li>
  </ul>

  <div class="abs consult-pill">Free Consultation<br>No Obligation</div>
  <p class="abs contact-script">Contact</p>
  <p class="abs contact-name nowrap">Marcus Whitfield <span>today at</span></p>

  <div class="abs agent-panel">
    <div class="abs skyline" role="img" aria-label="Photo of a city skyline at sunset"></div>
    <div class="abs contact-line" style="left:245px;top:19px;font-size:11.5px">
      <span class="mini-icon"><svg width="9" height="9" viewBox="0 0 24 24"><path d="M6.6 3.5l3 3.2-1.8 2.4c1 2.3 3 4.3 5.1 5.3l2.4-1.8 3.2 3-1.6 3.2C11 19 5 13 3.4 5.1z" fill="#fff"/></svg></span>(800) 641-2907 x 42
    </div>
    <div class="abs contact-line" style="left:240px;top:40px;font-size:7.5px;gap:4px">
      <span class="mini-icon"><svg width="9" height="9" viewBox="0 0 24 24"><rect x="3" y="6" width="18" height="12" fill="#fff"/><path d="M3 6l9 7 9-7" fill="none" stroke="#d9a24d" stroke-width="2"/></svg></span>mwhitfield@bluecovelending.com
    </div>
    <p class="abs agent-nmls">(NMLS #84617)</p>
  </div>

  <svg class="abs portrait" width="270" height="279" viewBox="0 0 270 279" role="img" aria-label="Portrait photo of the loan officer in a dark jacket and hat">
    <defs>
      <linearGradient id="portraitTone" x1="0" y1="0" x2="0" y2="1">
        <stop offset="0" stop-color="#3a3a3a"/>
        <stop offset="1" stop-color="#141414"/>
      </linearGradient>
    </defs>
    <path d="M66 40 C66 14 88 2 114 2 C140 2 162 14 162 40 L162 82 C200 92 228 112 240 150 L256 279 L38 279 L48 150 C54 112 62 96 66 82 Z" fill="url(#portraitTone)"/>
  </svg>
</section>

</body>
</html>
```